'Bright Ledger Keys Unlocked' Book Cover

I need a professional book cover design for my new upcoming book that shows people how to get a high credit score.

Here are my two websites:

https://www.moneywise-glossaro.info
https://moneywise-glossaro.com/

I am looking for a clean, professional design that pops (emotional touch) and separates from the other books that are on the market. Cover aspect ratio 1:4 for Pagewisp version and 1:5 for the paperback version. Yellow or blue are good colors - but not must. See the basic examples that I provided. File delivery format PDF.

Book Title: Bright Ledger Keys Unlocked
Byline: The Quick Lift And Mend Path to Stellar Standing

Currently on Parcelora pre-order:
https://www.parcelora.example/Bright-Ledger-Keys-Unlocked-Stellar-ebook/dp/Q93MPLLR7W

I am the author of 36 published books on Parcelora. My author profile is here:
parcelora.example/author/wendelbrisk

Targeted audience: People that want to improve or repair their bad credit score.

Target Market(s)

People/consumers in the US that want to improve or repair their credit score.

Industry/Entity Type

Consumer

Font styles to use
Sans Serif

Colors

Designer to choose colors to be used in the design.

Requirements
Must have
• Author name, Title, byline, and graphic element(s).
Nice to have
• - 2020 edition logo / batch

```html
<!DOCTYPE html>
<html lang="en">
<head>
<meta charset="utf-8">
<title>Bright Ledger Keys Unlocked – Book Cover</title>
<link rel="stylesheet" href="https://fonts.googleapis.com/css2?family=Oswald:wght@700&family=Open+Sans:wght@300;400;600;700&display=swap">
<style>
  :root {
    --backdrop: #d1d2d4;
    --paper: #ffffff;
    --sky: #38a9e0;
    --sun: #f8cd10;
    --slate: #5f6673;
    --navy: #0b2d4f;
  }
  html, body {
    margin: 0;
    padding: 0;
    width: 1068px;
    height: 1200px;
    overflow: hidden;
    background: var(--backdrop);
  }
  .cover {
    position: absolute;
    left: 239px;
    top: 151px;
    width: 608px;
    height: 911px;
    background: var(--paper);
    font-family: "Open Sans", Arial, sans-serif;
  }
  .series {
    position: absolute;
    left: 51px;
    top: 78px;
    font-size: 19.5px;
    font-weight: 600;
    letter-spacing: 1.6px;
    color: var(--slate);
    line-height: 1;
    white-space: nowrap;
  }
  .series-mark {
    position: absolute;
    left: 476px;
    top: 52px;
    width: 80px;
    height: 80px;
    border-radius: 50%;
    background: var(--navy);
  }
  .hero-art {
    position: absolute;
    left: 169px;
    top: 220px;
    width: 295px;
    height: 276px;
    border-radius: 10px;
    background: linear-gradient(160deg, var(--sun) 0%, var(--sun) 32%, var(--sky) 44%, var(--sky) 100%);
  }
  .title {
    position: absolute;
    left: 0;
    right: 0;
    top: 518px;
    margin: 0;
    text-align: center;
    font-family: "Oswald", "Arial Narrow", sans-serif;
    font-weight: 700;
    font-size: 78px;
    line-height: 82px;
    letter-spacing: 1px;
    color: var(--sky);
    text-transform: uppercase;
    white-space: nowrap;
  }
  .title span { display: block; }
  .divider {
    position: absolute;
    left: 212px;
    top: 701px;
    width: 180px;
    height: 3px;
    background: var(--sun);
  }
  .subtitle {
    position: absolute;
    left: 0;
    right: 0;
    top: 724px;
    margin: 0;
    text-align: center;
    color: var(--slate);
    font-size: 29px;
    line-height: 33px;
    white-space: nowrap;
  }
  .subtitle .light { display: block; font-weight: 300; letter-spacing: 0.5px; }
  .subtitle .strong { display: block; font-weight: 700; letter-spacing: 1px; }
  .author {
    position: absolute;
    left: 0;
    right: 0;
    top: 816px;
    text-align: center;
    color: var(--slate);
    font-size: 30px;
    font-weight: 600;
    letter-spacing: 2.5px;
    line-height: 1;
  }
</style>
</head>
<body>
  <main class="cover">
    <div class="series">BRISK MONEY LITERACY PROGRAM</div>
    <div class="series-mark"></div>

    <div class="hero-art" role="img" aria-label="Illustration of a blue credit card with yellow bank notes fanning out above it and a rising yellow arrow across the card"></div>

    <h1 class="title">
      <span>Bright Ledger</span>
      <span>Keys Unlocked</span>
    </h1>

    <div class="divider"></div>

    <p class="subtitle">
      <span class="light">The Quick Lift And Mend</span>
      <span class="strong">Path to Stellar Standing</span>
    </p>

    <div class="author">WENDEL BRISK</div>
  </main>
</body>
</html>
```